Create a business Card for a Women Owned Business Body Positive Company. The winner we hope to work with on other projects coming up for grand opening for flyers, postcards, email marketing, facebook page, stationary, labels, tshirt design....
We would like if possible in the background of the card a infinity symbol or crown if it fits into the design if not it's ok. But I am open to all suggestions we had alot problems with the our new logo being created this time sad to say :(

Our colors are Royal Purple, Grey, Black Thank you in advance for your talent, you hard work and your submissions!
Delia and Nadine :)
Updates

my Logo is velvet harbor boutique which is purple and has a heart and infinity sign in it and my colors are purple silver and black only of another card i had done nothing else. My logo is VELVET HARBOR BOUTIQUE LOGO

Industry/Entity Type

Retail

Contact Information for Business Card

website: www.velvtharborboutiques.example email: sales@velvetharborboutique.example
Delia Pruett & Nadine Kolb Owners

Font styles to use
Script

Colors
b768aa

Requirements
Must have
• COLORS ARE PURPLE BLACK AND GREY
Nice to have
• INFINITY SIGNING IN THE BACKGROUND

```html
<!DOCTYPE html>
<html lang="en">
<head>
<meta charset="utf-8">
<title>Velvet Harbor Boutique – Business Card</title>
<link rel="stylesheet" href="https://fonts.googleapis.com/css2?family=Cinzel:wght@400;500&family=Cormorant+Garamond:ital,wght@1,500&family=Roboto:wght@400&display=swap">
<style>
  :root {
    --royal-purple: #6a3f97;
    --card-white: #f3f3f3;
    --ink-black: #1c1c1c;
    --page-bg: #e6e4e8;
    --text-white: #ffffff;
  }
  html, body {
    margin: 0;
    padding: 0;
    width: 1200px;
    height: 960px;
    overflow: hidden;
    background: var(--page-bg);
  }
  .canvas {
    position: relative;
    width: 1200px;
    height: 960px;
  }
  .card {
    position: absolute;
    width: 600px;
    height: 343px;
    border-radius: 18px;
    overflow: hidden;
  }
  /* Front */
  .card-front {
    left: 314px;
    top: 113px;
    background: var(--card-white);
  }
  .front-swoosh {
    position: absolute;
    inset: 0;
    width: 600px;
    height: 343px;
  }
  .brand-name {
    position: absolute;
    left: 40px;
    top: 62px;
    width: 255px;
    margin: 0;
    text-align: center;
    font-family: "Cinzel", serif;
    font-weight: 500;
    font-size: 25px;
    line-height: 1.25;
    letter-spacing: 0.5px;
    color: var(--royal-purple);
  }
  .owners {
    position: absolute;
    right: 36px;
    top: 186px;
    text-align: right;
    font-family: "Cinzel", serif;
    font-weight: 500;
    color: var(--text-white);
  }
  .owners .owner-name {
    display: block;
    font-size: 21px;
    line-height: 26px;
  }
  .owners .owner-role {
    display: block;
    font-size: 16px;
    line-height: 24px;
    letter-spacing: 0.5px;
  }
  .contact {
    position: absolute;
    right: 33px;
    top: 270px;
    text-align: right;
    font-family: "Cormorant Garamond", serif;
    font-style: italic;
    font-weight: 500;
    font-size: 16px;
    line-height: 20px;
    color: var(--text-white);
  }
  /* Back */
  .card-back {
    left: 311px;
    top: 472px;
    background: var(--royal-purple);
  }
  .back-name {
    position: absolute;
    left: 0;
    right: 0;
    top: 118px;
    margin: 0;
    text-align: center;
    font-family: "Cinzel", serif;
    font-weight: 400;
    font-size: 36px;
    letter-spacing: 0.5px;
    color: var(--text-white);
  }
  .web-band {
    position: absolute;
    left: 0;
    right: 0;
    top: 277px;
    height: 33px;
    background: var(--card-white);
    display: flex;
    align-items: center;
    justify-content: center;
    font-family: "Roboto", sans-serif;
    font-size: 15px;
    letter-spacing: 4px;
    color: var(--royal-purple);
  }
</style>
</head>
<body>
<main class="canvas">

  <section class="card card-front">
    <svg class="front-swoosh" viewBox="0 0 600 343" aria-hidden="true">
      <path d="M330 0 C392 45 378 135 308 212 C262 264 238 306 244 343 L600 343 L600 0 Z" fill="var(--royal-purple)"/>
      <path d="M342 12 C388 62 366 150 300 222 C258 268 236 300 238 322 C232 296 246 258 290 212 C352 146 376 70 342 12 Z" fill="var(--ink-black)"/>
      <path d="M346 28 C374 80 356 158 296 232 C266 270 252 298 250 316 C256 292 272 266 304 228 C360 160 378 84 346 28 Z" fill="var(--card-white)"/>
    </svg>
    <h1 class="brand-name">Velvet Harbor<br>Boutique</h1>
    <p class="owners">
      <span class="owner-name">Delia Pruett</span>
      <span class="owner-name">Nadine Kolb</span>
      <span class="owner-role">Owners</span>
    </p>
    <p class="contact">
      sales@velvetharborboutique.example<br>
      www.velvtharborboutiques.example
    </p>
  </section>

  <section class="card card-back">
    <h2 class="back-name">VELVET HARBOR BOUTIQUE</h2>
    <div class="web-band">www.velvtharborboutiques.example</div>
  </section>

</main>
</body>
</html>
```